skincare creams for tired moms

I need a package and a logo design for a skincare company based in California called Dawn Meadow. I make day and night cream, under eye cream, and body lotion. The first product I plan to launch is an under eye cream. It does not have to be in these colors but I do teals, greens, black, and cobalt blue.

The package is going to either be in a box or a bag. Either way I go it will be like a gift box or bag. The design should make the person feel like they are getting something special and luxurious just for them.

I have small kids and it is really difficult to find a chunk of time to myself to update or review.

Target Market(s)

mainly first time moms. I am making an under eye cream that does not use retinol but is still powerful enough to get rid of bags and dark circles.

Industry/Entity Type

Cosmetics

Logo Text

The package and logo should incorporate the name Dawn Meadow.

Font styles to use
Decorative
Script

Colors

Designer to choose colors to be used in the design.

Requirements
Nice to have
• maybe focus more on Meadow instead of Dawn. Also incorporate plants or flowers
Should not have
• not a huge fan of pink

```html
<!DOCTYPE html>
<html lang="en">
<head>
<meta charset="utf-8">
<title>Dawn Meadow Eye Cream Label</title>
<link rel="stylesheet" href="https://fonts.googleapis.com/css2?family=Great+Vibes&family=Lato:wght@400&display=swap">
<style>
  :root {
    --backdrop: #ededed;
    --label-green: #4f6f22;
    --label-green-deep: #46651d;
    --leaf-tint: #5f7f33;
    --ink-light: #f3f1e8;
  }
  html, body {
    margin: 0;
    padding: 0;
    width: 900px;
    height: 1200px;
    overflow: hidden;
    background: var(--backdrop);
  }
  .canvas {
    position: relative;
    width: 900px;
    height: 1200px;
  }
  .label {
    position: absolute;
    left: 180px;
    top: 40px;
    width: 540px;
    height: 1120px;
    background: linear-gradient(180deg, var(--label-green) 0%, var(--label-green-deep) 100%);
    overflow: hidden;
    color: var(--ink-light);
    text-align: center;
  }
  .leaf-decoration {
    position: absolute;
    left: -40px;
    top: 430px;
    width: 300px;
    height: 480px;
    border-radius: 50%;
    background: radial-gradient(ellipse at 40% 50%, var(--leaf-tint) 0%, rgba(95,127,51,0) 70%);
    opacity: 0.8;
  }
  .brand-name {
    position: absolute;
    top: 250px;
    left: 0;
    right: 0;
    margin: 0;
    font-family: "Great Vibes", cursive;
    font-weight: 400;
    font-size: 82px;
    line-height: 1;
  }
  .product-title {
    position: absolute;
    top: 500px;
    left: 0;
    right: 0;
    margin: 0;
    font-family: "Great Vibes", cursive;
    font-weight: 400;
    line-height: 1;
  }
  .product-title .word-eye {
    display: block;
    font-size: 70px;
    margin-left: 40px;
  }
  .product-title .word-cream {
    display: block;
    font-size: 130px;
    margin-top: -30px;
  }
  .title-rule {
    position: absolute;
    top: 728px;
    left: 245px;
    width: 50px;
    height: 5px;
    background: var(--ink-light);
  }
  .ingredients, .benefit, .volume {
    position: absolute;
    left: 0;
    right: 0;
    margin: 0;
    font-family: "Lato", sans-serif;
    font-weight: 400;
  }
  .ingredients {
    top: 768px;
    font-size: 30px;
    line-height: 1.45;
  }
  .benefit {
    top: 880px;
    font-size: 30px;
  }
  .volume {
    top: 1040px;
    font-size: 28px;
  }
</style>
</head>
<body>
  <main class="canvas">
    <section class="label">
      <div class="leaf-decoration" role="img" aria-label="Faint decorative leaves in the background"></div>
      <h1 class="brand-name">Dawn Meadow</h1>
      <h2 class="product-title">
        <span class="word-eye">Eye</span>
        <span class="word-cream">Cream</span>
      </h2>
      <div class="title-rule"></div>
      <p class="ingredients">Hyaluronic Acid<br>Collagen, Caffeine</p>
      <p class="benefit">Moisturize &amp; Regenerate</p>
      <p class="volume">0.5 oz / 15 ml</p>
    </section>
  </main>
</body>
</html>
```